依頼詳細
大通りに面していて車で走りながら見てすぐにわかるように、かつ目を引く看板のデザインがいいです。ターゲット層は20才から年配の方までは幅広いですがシンプルで温かみがありわかりやすいデザインを希望します。
記載項目
サイズ:横100cm×縦420cm
建物全体の色が白系統となります。「ギフト専門店」「贈答品専門店」「贈答品」「ギフト」などの何のお店なのか分かる必要があります。また、結婚内祝・出産内祝・景品・香典返しの文言を組み込んで欲しいです。
希望イメージ
シンプル 複雑
単色 カラフル
暗い 明るい
日常 高級
遊び心 厳粛
未来的 伝統的
女性的 男性的
希望する色
特にないですが、店舗全体の色が白系統です。
納品ファイル
• イラストレーター形式 (.ai)
補足説明
イメージデータはハコブネ転送にアップロードしました。
https://73.hakobune-sd.jp/0528-c3d1e8a0f4b72a903e1c5d6084b2f7e6
現在の外観写真を添付します。

シンプルですが、伝えたいことが分かる視認性を重視しました。

この度はコンペ参加ありがとうございます。今後ともよろしくお願いします。

```html
<!DOCTYPE html>
<html lang="ja">
<head>
<meta charset="utf-8">
<title>ギフト専門店 縦看板</title>
<link rel="stylesheet" href="https://fonts.googleapis.com/css2?family=Dela+Gothic+One&family=Noto+Sans+JP:wght@700;900&display=swap">
<style>
  :root {
    --brand-red: #b3252b;
    --sign-white: #ffffff;
  }
  * { margin: 0; padding: 0; box-sizing: border-box; }
  html, body {
    width: 1200px;
    height: 5048px;
    overflow: hidden;
    background: var(--sign-white);
  }
  .sign {
    position: relative;
    width: 1200px;
    height: 5048px;
    background: var(--sign-white);
    font-family: "Noto Sans JP", sans-serif;
  }
  .gift-mark {
    position: absolute;
    left: 152px;
    top: 120px;
    width: 912px;
    height: 928px;
    border-radius: 64px;
    background: var(--brand-red);
  }
  .shop-band {
    position: absolute;
    left: 0;
    top: 1192px;
    width: 1200px;
    height: 1228px;
    background: var(--brand-red);
    color: var(--sign-white);
    text-align: center;
  }
  .shop-band__gift {
    position: absolute;
    left: 0;
    top: 60px;
    width: 100%;
    font-family: "Dela Gothic One", sans-serif;
    font-size: 300px;
    line-height: 1;
    letter-spacing: 10px;
  }
  .shop-band__kind {
    position: absolute;
    left: 0;
    top: 330px;
    width: 100%;
    font-weight: 700;
    font-size: 232px;
    line-height: 1;
  }
  .shop-band__cord {
    position: absolute;
    left: 0;
    top: 1080px;
    width: 100%;
    height: 14px;
    background: var(--sign-white);
  }
  .shop-band__knot {
    position: absolute;
    left: 470px;
    top: 880px;
    width: 260px;
    height: 220px;
    border-radius: 40px 40px 16px 16px;
    background: linear-gradient(#c9494e, #f3dcdc);
  }
  .occasion {
    position: absolute;
    left: 0;
    width: 100%;
    text-align: center;
    color: var(--brand-red);
    font-weight: 900;
    font-size: 262px;
    line-height: 1;
  }
  .occasion--wedding { top: 2468px; }
  .occasion--birth { top: 3148px; }
  .occasion--prize { top: 3828px; }
  .occasion--memorial { top: 4508px; }
  .divider {
    position: absolute;
    left: 0;
    width: 1200px;
    height: 252px;
    background: var(--brand-red);
  }
  .divider--1 { top: 2820px; }
  .divider--2 { top: 3500px; }
  .divider--3 { top: 4180px; }
  .divider__icon {
    position: absolute;
    left: 520px;
    top: 46px;
    width: 160px;
    height: 160px;
    border-radius: 50%;
    background: rgba(255, 255, 255, 0.85);
  }
</style>
</head>
<body>
  <div class="sign">
    <div class="gift-mark" role="img" aria-label="桜の花と帯をあしらった贈り物の箱のマーク"></div>

    <div class="shop-band">
      <div class="shop-band__gift">ギフト</div>
      <div class="shop-band__kind">専門店</div>
      <div class="shop-band__knot" role="img" aria-label="水引の結び飾り"></div>
      <div class="shop-band__cord"></div>
    </div>

    <div class="occasion occasion--wedding">結婚内祝</div>
    <div class="divider divider--1">
      <div class="divider__icon" role="img" aria-label="赤ちゃんのアイコン"></div>
    </div>

    <div class="occasion occasion--birth">出産内祝</div>
    <div class="divider divider--2">
      <div class="divider__icon" role="img" aria-label="景品を掲げる人のアイコン"></div>
    </div>

    <div class="occasion occasion--prize">景品</div>
    <div class="divider divider--3">
      <div class="divider__icon" role="img" aria-label="蓮の花のアイコン"></div>
    </div>

    <div class="occasion occasion--memorial">香典返礼</div>
  </div>
</body>
</html>
```